Brava Nest (Smart Home, Installation, Repair Industry) (Contest)

Looking for a website design for my company
Services we offer:
Phone Repair
TV Mounting
Security Camera Installation
Networking / Wi-Fi
Smart Home Services
IT Support

Looking for a website similar to trovely.example

Few tabs
About Us
Contact Us
Areas Served
Pricing and Services

```html
<!DOCTYPE html>
<html lang="en">
<head>
<meta charset="utf-8">
<title>Brava Nest — Technicians in your Neighborhood</title>
<link href="https://fonts.googleapis.com/css2?family=Poppins:wght@300;400;500;600;700&display=swap" rel="stylesheet">
<style>
:root{
  --ink:#37325f;
  --ink-deep:#2b2f5e;
  --body:#6b6a80;
  --orange:#f7931e;
  --violet:#9166d4;
  --mint:#5fd38d;
  --navy:#232a55;
  --footer:#2c3262;
  --mist:#f4f4f9;
  --line:#e4e4ee;
  --white:#ffffff;
}
*{margin:0;padding:0;box-sizing:border-box}
html,body{width:1200px;height:2799px;overflow:hidden}
body{position:relative;background:#fcfcfe;font-family:'Poppins',sans-serif;color:var(--ink)}
.abs{position:absolute}
.hero-bg{left:0;top:0;width:1200px;height:600px}
.brand{font-weight:700;font-size:25px;color:var(--orange);letter-spacing:-.3px}
.nav{top:38px;left:489px;display:flex;gap:29px;font-size:14px;color:var(--white);font-weight:400}
.social-top{top:45px;left:931px;display:flex;gap:7px}
.social-top span{width:8px;height:8px;border-radius:50%;background:var(--white);display:block}
.hero-title{top:193px;width:1200px;text-align:center;color:var(--white);font-size:39px;line-height:48px}
.hero-title b{font-weight:700;letter-spacing:-.8px}
.hero-title span{font-weight:300;letter-spacing:-1px}
.hero-sub{top:308px;width:1200px;text-align:center;color:#e6e4f5;font-size:15px;font-weight:300}
.btn{top:371px;left:534px;width:131px;height:35px;background:var(--orange);color:var(--white);font-size:12px;font-weight:600;display:flex;align-items:center;justify-content:center;border-radius:2px}
.section-head{width:1200px;text-align:center;font-size:20px;line-height:26px;font-weight:400;color:var(--ink-deep)}
.card{top:742px;width:171px;height:194px;background:var(--white);border:1px solid var(--line);border-radius:3px;text-align:center}
.card.active{border-top:3px solid var(--orange);box-shadow:0 8px 22px rgba(40,40,90,.09)}
.card svg{margin-top:30px}
.card h3{font-size:12px;font-weight:600;line-height:17px;margin-top:14px;color:var(--ink-deep);padding:0 14px}
.card p{font-size:11px;line-height:17px;color:var(--body);margin-top:14px;padding:0 26px}
.dot{top:961px;width:6px;height:6px;border-radius:50%;background:#b3b6d0}
.dot.on{background:var(--orange)}
.feature h2{font-size:30px;font-weight:700;line-height:36px;color:var(--ink);letter-spacing:-.6px}
.feature h2 span{display:block;font-weight:300}
.feature p{font-size:12px;line-height:23px;color:var(--body);margin-top:16px}
.block{border-radius:1px}
.faq-band{left:0;top:1697px;width:1200px;height:401px;background:var(--mist)}
.faq{top:1853px;width:234px;height:170px;background:var(--white);border:1px solid var(--line);border-radius:3px;padding:28px 32px}
.faq.active{border-top:3px solid #dcdce6;box-shadow:0 8px 22px rgba(40,40,90,.09)}
.faq h4{font-size:12px;font-weight:600;color:var(--ink-deep);display:flex;justify-content:space-between;align-items:center}
.faq h4 i{width:16px;height:16px;border-radius:50%;font-style:normal;color:var(--white);font-size:9px;display:flex;align-items:center;justify-content:center}
.faq p{font-size:11px;line-height:19px;color:var(--body);margin-top:18px}
.quote{top:2350px;width:1200px;text-align:center;font-size:11.5px;line-height:23px;color:var(--body)}
.quote-name{top:2402px;width:1200px;text-align:center;font-size:11.5px;color:var(--body)}
.footer-line{left:229px;top:2710px;width:742px;height:1px;background:#8a8fb3}
.copy{top:2745px;width:1200px;text-align:center;font-size:11px;color:#b7bad4}
.copy b{color:var(--orange);font-weight:500}
.foot-social{top:2646px;left:877px;display:flex;gap:7px}
.foot-social span{width:26px;height:26px;border-radius:50%;background:#5a5f86;display:block}
</style>
</head>
<body>

<svg class="abs hero-bg" viewBox="0 0 1200 600" role="img" aria-label="Photo of a smiling technician in a denim shirt in a workshop, with a violet overlay">
  <defs>
    <linearGradient id="heroTone" x1="0" y1="0" x2="1" y2="1">
      <stop offset="0" stop-color="#7572ad"/>
      <stop offset=".55" stop-color="#5f5c9e"/>
      <stop offset="1" stop-color="#3f4283"/>
    </linearGradient>
  </defs>
  <path d="M0 0H1200V593C1000 576 800 572 600 575C380 579 180 585 0 598Z" fill="url(#heroTone)"/>
</svg>

<div class="abs brand" style="left:230px;top:30px;color:var(--orange)">Brava Nest</div>
<nav class="abs nav"><span>About Us</span><span>Pricing &amp; Services</span><span>Areas Served</span><span>Contact</span></nav>
<div class="abs social-top"><span></span><span></span><span></span></div>

<h1 class="abs hero-title"><b>The Best Technicians</b><br><span>in your Neighborhood.</span></h1>
<p class="abs hero-sub">The best technicians in your neighborhood.</p>
<div class="abs btn">Book a Service</div>

<h2 class="abs section-head" style="top:658px">Brava Nest is pretty big thing to explore<br>Checkout Services</h2>

<div class="abs card" style="left:229px">
  <svg width="44" height="44" viewBox="0 0 44 44" fill="none" stroke="#55597a" stroke-width="1.6"><rect x="5" y="4" width="20" height="36" rx="2"/><rect x="14" y="8" width="20" height="32" rx="2"/><path d="M34 6a6 6 0 0 1 5 5M34 10a3 3 0 0 1 2 2"/><circle cx="9" cy="10" r="1"/><circle cx="9" cy="14" r="1"/></svg>
  <h3>Phone Repair</h3>
  <p>Fix your phone at your home, office</p>
</div>
<div class="abs card active" style="left:419px">
  <svg width="48" height="44" viewBox="0 0 48 44" fill="none" stroke="#f7931e" stroke-width="1.8"><rect x="3" y="5" width="42" height="28" rx="2"/><rect x="7" y="9" width="34" height="20"/><path d="M18 33v5M30 33v5M12 39h24"/></svg>
  <h3>TV Mounting</h3>
  <p>Let us do the heavy lifting for yourm new TV</p>
</div>
<div class="abs card" style="left:610px">
  <svg width="50" height="44" viewBox="0 0 50 44" fill="none" stroke="#55597a" stroke-width="1.6"><path d="M14 8l30 10-6 9-26-9z"/><path d="M20 23l-4 8H8M4 25v14M4 32h4"/><circle cx="34" cy="19" r="1.5"/></svg>
  <h3>Security Camera Installation</h3>
  <p>Lorem Ipsum is simply</p>
</div>
<div class="abs card" style="left:800px">
  <svg width="52" height="44" viewBox="0 0 52 44" fill="none" stroke="#55597a" stroke-width="1.6"><path d="M4 16a30 30 0 0 1 40 0M9 21a22 22 0 0 1 30 0M14 26a14 14 0 0 1 20 0"/><circle cx="22" cy="34" r="3"/><circle cx="42" cy="28" r="3"/><path d="M42 31v9M26 40a6 6 0 0 1 10 0"/></svg>
  <h3>Networking / Wi-Fi</h3>
  <p>Lorem Ipsum is simply dummy text of the</p>
</div>

<span class="abs dot" style="left:622px"></span>
<span class="abs dot on" style="left:636px"></span>
<span class="abs dot" style="left:650px"></span>

<div class="abs feature" style="left:643px;top:1043px;width:320px">
  <h2>Trusted technicians<span>in your neighborhood</span></h2>
  <p>Lorem Ipsum is simply dummy text of the printing and typesetting industry. Lorem Ipsum has been the industry's standard dummy text ever since the 1500s,</p>
</div>

<div class="abs" style="left:240px;top:1342px;width:260px;height:14px;border-radius:50%;background:radial-gradient(ellipse,rgba(60,60,100,.12),transparent 70%)"></div>
<div class="abs" style="left:650px;top:1517px;width:300px;height:14px;border-radius:50%;background:radial-gradient(ellipse,rgba(60,60,100,.12),transparent 70%)"></div>

<div class="abs block" style="left:441px;top:1138px;width:159px;height:174px;background:var(--orange)"></div>
<div class="abs block" style="left:619px;top:1229px;width:63px;height:67px;background:var(--violet)"></div>
<div class="abs block" style="left:518px;top:1331px;width:63px;height:68px;background:var(--mint)"></div>
<div class="abs block" style="left:601px;top:1315px;width:158px;height:174px;background:var(--navy)"></div>

<div class="abs feature" style="left:229px;top:1422px;width:332px;text-align:right">
  <h2>Guaranteed Parts<span>&amp; service + 24/7 support</span></h2>
  <p>It is important to stay focused on saving money in any way you can. We help you monitor your spending habits so you can easily spot and cut any unnecessary expenses. Simply join today to get started!</p>
</div>

<div class="abs faq-band"></div>
<h2 class="abs section-head" style="top:1768px">Do you have any questions?<br>Findout answers:</h2>

<div class="abs faq" style="left:229px">
  <h4>Lorem Ipsum is simply <i style="background:#a597e0">?</i></h4>
  <p>Lorem Ipsum is simply dummy text of the printing and typesetting industry. Lorem Ipsum has been the industry's text ever</p>
</div>
<div class="abs faq active" style="left:483px">
  <h4>Lorem Ipsum is simply <i style="background:#f9b640">?</i></h4>
  <p>Lorem Ipsum is simply dummy text of the printing and typesetting industry. Lorem Ipsum has been the industry's text ever</p>
</div>
<div class="abs faq" style="left:737px">
  <h4>Lorem Ipsum is simply <i style="background:#f58aa8">?</i></h4>
  <p>Lorem Ipsum is simply dummy text of the printing and typesetting industry. Lorem Ipsum has been the industry's text ever</p>
</div>

<h2 class="abs section-head" style="top:2155px">What users think about<br>Users testimonails:</h2>

<svg class="abs" style="left:380px;top:2230px" width="460" height="110" viewBox="0 0 460 110">
  <circle cx="19" cy="51" r="13" fill="#fff" stroke="#e6e6ee"/>
  <path d="M21 47l-4 4 4 4" fill="none" stroke="#8a8ca5" stroke-width="1.2"/>
  <circle cx="438" cy="51" r="13" fill="#fff" stroke="#e6e6ee"/>
  <path d="M436 47l4 4-4 4" fill="none" stroke="#8a8ca5" stroke-width="1.2"/>
  <circle cx="170" cy="51" r="27" fill="#ececf0"/>
  <circle cx="290" cy="51" r="27" fill="#ececf0"/>
  <circle cx="228" cy="51" r="41" fill="#cfcfd4" role="img" aria-label="Customer portrait"/>
  <circle cx="228" cy="87" r="15" fill="var(--orange)" stroke="#fff" stroke-width="3"/>
  <text x="228" y="92" text-anchor="middle" font-family="Poppins,sans-serif" font-weight="700" font-size="13" fill="#fff">“</text>
</svg>

<p class="abs quote">Lorem Ipsum is simply dummy text of the printing and typesetting industry. Lorem Ipsum<br>has been the industry's standard dummy text ever since the 1500s,</p>
<p class="abs quote-name">Lorem Ipsum</p>

<svg class="abs" style="left:578px;top:2443px" width="50" height="10" viewBox="0 0 50 10">
  <circle cx="5" cy="5" r="3" fill="none" stroke="var(--orange)" stroke-width="1.2"/>
  <circle cx="16" cy="5" r="1.6" fill="#c4c6d8"/><circle cx="25" cy="5" r="1.6" fill="#c4c6d8"/>
  <circle cx="34" cy="5" r="1.6" fill="#c4c6d8"/><circle cx="43" cy="5" r="1.6" fill="#c4c6d8"/>
</svg>

<svg class="abs" style="left:0;top:2470px" width="1200" height="329" viewBox="0 0 1200 329">
  <path d="M0 120C60 40 140 0 200 20C270 40 320 130 420 147C520 165 580 95 660 50C740 5 820 20 900 75C980 130 1080 140 1200 20V329H0Z" fill="var(--footer)"/>
</svg>

<div class="abs brand" style="left:231px;top:2644px">Brava Nest</div>
<div class="abs foot-social"><span></span><span></span><span></span></div>
<div class="abs footer-line"></div>
<p class="abs copy">© All 2020 All rights reserved &nbsp;<b>Brava Nest</b></p>

</body>
</html>
```